DL Flyer,A4 letterhead, with compliments slip, and envelopes
For new safety consultancy business
DL Flyer,A4 letterhead, with compliments slip, and envelopes - Consulting
Creative Brief
Yes
New safety consultancy in Australia, focussing on small to medium industrial businesses.
Modern
Unsure - similar to logo maybe?
DL size FLYER TO be one sided glossy to INCLUDE FOLLOWING WORDS:
Occupational Health and Safety is a minefield of laws and regulations for the unprepared employer. Did you know that no matter how small an employer you are, by law you still need a safety management system? Did you know that you need specific procedures in place to prove that your employees, contractors and visitors are safe?
Let Hazardwell implement an OHS strategy that is cost effective and right for you.
Our services not only include OHS advice but also the development of:
- OHS management systems
- Risk assessments
- Safe work method statements
- Checklists, forms and registers
- Training and toolbox talks
Hazardwell is a local business, accredited in auditing Australian Standard 4801 OHS management systems. To arrange a free OHS pulse check of your systems and find out if you meet legislation, call Hazardwell now on 0418 264 907.
info@hazardwellexample.com.au
www.hazardwellexample.com.au
LETTER HEAD TO INCLUDE following company details:
Company name: Hazardwell
Address: PO Box 58, Brindlemoor NSW 2391
Phone: 0418 264 907
Email: info@hazardwellexample.com.au
Web: www.hazardwellexample.com.au

```html
<!DOCTYPE html>
<html lang="en">
<head>
<meta charset="utf-8">
<title>Hazardwell Stationery Suite</title>
<link href="https://fonts.googleapis.com/css2?family=Open+Sans:wght@400;700;800&family=Great+Vibes&display=swap" rel="stylesheet">
<style>
  :root {
    --bg: #e9e6e1;
    --paper: #ffffff;
    --green: #2f9a3b;
    --green-dark: #1d6f2a;
    --green-light: #7dc243;
    --ink: #333333;
    --muted: #777777;
    --yellow: #f6d21c;
    --shadow: 0 2px 6px rgba(0,0,0,.18);
  }
  * { box-sizing: border-box; margin: 0; padding: 0; }
  html, body { width: 1200px; height: 514px; overflow: hidden; }
  body { background: var(--bg); font-family: "Open Sans", Arial, sans-serif; color: var(--ink); position: relative; }
  .piece { position: absolute; background: var(--paper); box-shadow: var(--shadow); overflow: hidden; }
  .swoosh { position: absolute; left: 0; bottom: 0; width: 100%; display: block; }
  .brand { font-weight: 800; color: var(--green); letter-spacing: -.2px; display: flex; align-items: center; gap: 4px; line-height: 1; }
  .brand-dot { width: .7em; height: .7em; border-radius: 50%; background: var(--green); display: inline-block; }
  .contact { position: absolute; color: #fff; font-size: 4.5px; line-height: 1.5; z-index: 1; }

  /* business cards */
  .card { width: 140px; height: 80px; }
  .card-back { left: 62px; top: 172px; background: var(--green); }
  .card-back .brand { color: #fff; font-size: 13px; position: absolute; left: 14px; top: 20px; }
  .card-front { left: 96px; top: 236px; }
  .card-front .brand { font-size: 12px; position: absolute; left: 10px; top: 10px; }
  .card-front .person { position: absolute; left: 10px; top: 28px; font-size: 5px; color: var(--ink); line-height: 1.5; }

  /* compliments slip */
  .slip { left: 67px; top: 318px; width: 200px; height: 110px; }
  .slip .brand { font-size: 12px; position: absolute; left: 12px; top: 10px; }
  .slip .greeting { position: absolute; left: 56px; top: 42px; font-family: "Great Vibes", cursive; font-size: 20px; color: var(--ink); }

  /* letterhead */
  .letterhead { left: 295px; top: 77px; width: 236px; height: 356px; }
  .letterhead .brand { font-size: 16px; position: absolute; left: 20px; top: 20px; }
  .letterhead .faint-mark { position: absolute; left: 78px; top: 130px; width: 80px; height: 80px; border-radius: 50%; background: var(--green); opacity: .07; }
  .letterhead .contact { left: 20px; bottom: 5px; }

  /* DL flyer */
  .flyer { left: 626px; top: 152px; width: 132px; height: 288px; }
  .flyer .brand { font-size: 12px; position: absolute; left: 8px; top: 8px; }
  .flyer-copy { position: absolute; left: 8px; top: 28px; width: 82px; font-size: 3.6px; line-height: 1.45; color: var(--ink); }
  .flyer-copy p { margin-bottom: 3px; }
  .flyer-copy ul { list-style: none; margin-bottom: 3px; }
  .flyer-copy li::before { content: "\2713 "; color: var(--green); font-weight: 700; }
  .flyer .sign-art { position: absolute; right: 0; top: 100px; width: 40px; height: 72px; background: linear-gradient(160deg, var(--yellow), #d9a900); }
  .flyer-foot { position: absolute; left: 0; bottom: 0; width: 100%; height: 58px; background: var(--yellow); }
  .flyer-foot .hazard-art { position: absolute; left: 6px; top: 6px; width: 44px; height: 34px; background: linear-gradient(135deg, #2b2b2b, #5a5a3a); }
  .flyer-foot .callout { position: absolute; left: 56px; top: 10px; width: 70px; font-size: 4.2px; font-weight: 700; color: var(--green-dark); line-height: 1.4; }
  .flyer-foot .web { position: absolute; left: 0; bottom: 0; width: 100%; height: 11px; background: var(--green); color: #fff; font-size: 5px; font-weight: 700; text-align: center; line-height: 11px; }

  /* envelopes */
  .envelope { width: 330px; height: 118px; }
  .envelope-back { left: 778px; top: 200px; }
  .envelope-back .flap { position: absolute; left: 0; top: 0; width: 100%; height: 60px; display: block; }
  .envelope-back .brand { font-size: 11px; position: absolute; left: 130px; top: 8px; }
  .envelope-front { left: 778px; top: 325px; }
  .envelope-front .brand { font-size: 13px; position: absolute; left: 14px; top: 12px; }
</style>
</head>
<body>

  <!-- Business card, reverse -->
  <div class="piece card card-back">
    <div class="brand">Hazardwell<span class="brand-dot" style="background:#fff"></span></div>
    <svg class="swoosh" viewBox="0 0 140 30" height="30" preserveAspectRatio="none">
      <path d="M0 18 Q70 4 140 14 L140 30 L0 30 Z" fill="var(--green-dark)"/>
    </svg>
  </div>

  <!-- Business card, front -->
  <div class="piece card card-front">
    <div class="brand">Hazardwell<span class="brand-dot"></span></div>
    <div class="person"><strong>Molly Fern</strong><br>Director &amp; OHS Consultant<br>mollyfern@hazardwellexample.com.au</div>
    <svg class="swoosh" viewBox="0 0 140 24" height="24" preserveAspectRatio="none">
      <path d="M0 14 Q70 0 140 10 L140 24 L0 24 Z" fill="var(--green)"/>
    </svg>
    <div class="contact" style="left:60px;bottom:3px">0418 264 907</div>
  </div>

  <!-- Compliments slip -->
  <div class="piece slip">
    <div class="brand">Hazardwell<span class="brand-dot"></span></div>
    <div class="greeting">With Compliments</div>
    <svg class="swoosh" viewBox="0 0 200 26" height="26" preserveAspectRatio="none">
      <path d="M0 16 Q100 0 200 12 L200 26 L0 26 Z" fill="var(--green)"/>
      <path d="M0 16 Q100 0 200 12 L200 14 Q100 4 0 19 Z" fill="var(--green-light)"/>
    </svg>
    <div class="contact" style="left:12px;bottom:3px">PO Box 58, Brindlemoor NSW 2391 &nbsp;|&nbsp; 0418 264 907 &nbsp;|&nbsp; www.hazardwellexample.com.au</div>
  </div>

  <!-- A4 letterhead -->
  <div class="piece letterhead">
    <div class="brand">Hazardwell<span class="brand-dot"></span></div>
    <div class="faint-mark"></div>
    <svg class="swoosh" viewBox="0 0 236 64" height="64" preserveAspectRatio="none">
      <path d="M0 22 Q118 0 236 18 L236 64 L0 64 Z" fill="var(--green)"/>
      <path d="M0 22 Q118 0 236 18 L236 21 Q118 5 0 26 Z" fill="var(--green-light)"/>
    </svg>
    <div class="contact">PO Box 58, Brindlemoor NSW 2391<br>P 0418 264 907<br>E info@hazardwellexample.com.au<br>W www.hazardwellexample.com.au</div>
  </div>

  <!-- DL flyer -->
  <div class="piece flyer">
    <div class="brand">Hazardwell<span class="brand-dot"></span></div>
    <div class="flyer-copy">
      <p>Occupational Health and Safety is a minefield of laws and regulations for the unprepared employer. Did you know that no matter how small an employer you are, by law you still need a safety management system? Did you know that you need specific procedures in place to prove that your employees, contractors and visitors are safe?</p>
      <p><strong>Let Hazardwell implement an OHS strategy that is cost effective and right for you.</strong></p>
      <p>Our services not only include OHS advice but also the development of:</p>
      <ul>
        <li>OHS management systems</li>
        <li>Risk assessments</li>
        <li>Safe work method statements</li>
        <li>Checklists, forms and registers</li>
        <li>Training and toolbox talks</li>
      </ul>
      <p>Hazardwell is a local business, accredited in auditing Australian Standard 4801 OHS management systems.</p>
    </div>
    <div class="sign-art" role="img" aria-label="Yellow road warning sign illustration reading risk ahead"></div>
    <div class="flyer-foot">
      <div class="hazard-art" role="img" aria-label="Hazard warning signs illustration"></div>
      <div class="callout">To arrange a free OHS pulse check of your systems, call Hazardwell now on 0418 264 907.<br>info@hazardwellexample.com.au</div>
      <div class="web">www.hazardwellexample.com.au</div>
    </div>
  </div>

  <!-- Envelope, back with flap -->
  <div class="piece envelope envelope-back">
    <svg class="flap" viewBox="0 0 330 60" preserveAspectRatio="none">
      <path d="M0 0 L330 0 L330 12 L190 56 Q165 62 140 56 L0 12 Z" fill="#f4f4f4" stroke="#dddddd" stroke-width="1"/>
    </svg>
    <div class="brand">Hazardwell<span class="brand-dot"></span></div>
    <svg class="swoosh" viewBox="0 0 330 30" height="30" preserveAspectRatio="none">
      <path d="M0 14 Q165 0 330 10 L330 30 L0 30 Z" fill="var(--green)"/>
    </svg>
  </div>

  <!-- Envelope, front -->
  <div class="piece envelope envelope-front">
    <div class="brand">Hazardwell<span class="brand-dot"></span></div>
    <svg class="swoosh" viewBox="0 0 330 30" height="30" preserveAspectRatio="none">
      <path d="M0 16 Q165 0 330 12 L330 30 L0 30 Z" fill="var(--green)"/>
      <path d="M0 16 Q165 0 330 12 L330 15 Q165 4 0 20 Z" fill="var(--green-light)"/>
    </svg>
    <div class="contact" style="left:14px;bottom:4px">PO Box 58, Brindlemoor NSW 2391 &nbsp;|&nbsp; www.hazardwellexample.com.au</div>
  </div>

</body>
</html>
```